Visitenkarten-Design für Kfz-Werkstatt von Frauen für Frauen
Zielgruppe
Kfz-Werkstatt von Frauen für Frauen
Aufgabenstellung
Die Farben des Logos sollen sich in der Visitenkarte wieder spiegeln. Darf sehr feminin gehalten werden!
Infos auf der Visistenkarte:

```html
<!DOCTYPE html>
<html lang="de">
<head>
<meta charset="utf-8">
<title>Visitenkarte – Veltrinar</title>
<link href="https://fonts.googleapis.com/css2?family=Michroma&family=Lato:wght@400;700&display=swap" rel="stylesheet">
<style>
  :root {
    --backdrop: #ebe6e7;
    --card: #ffffff;
    --card-fade: #f3f3f3;
    --graphite: #5a5a5a;
    --rule: #6b6b6b;
    --lip-pink: #e0527f;
    --lip-soft: #f2b6c6;
    --band-start: #e27aa4;
    --band-end: #dc2a3a;
  }
  * { margin: 0; padding: 0; box-sizing: border-box; }
  html, body { width: 1200px; height: 1200px; overflow: hidden; }
  body { background: var(--backdrop); position: relative; font-family: "Lato", sans-serif; }

  .card {
    position: absolute;
    width: 718px;
    height: 466px;
    background: linear-gradient(to bottom, var(--card) 0%, var(--card) 30%, var(--card-fade) 100%);
    box-shadow: 0 6px 22px rgba(60, 40, 45, 0.25);
    overflow: hidden;
  }
  .card--front { left: 189px; top: 111px; }
  .card--back { left: 342px; top: 637px; }

  .front-rule {
    position: absolute; left: 0; right: 0; top: 282px;
    height: 3px; background: var(--rule);
  }
  .front-name {
    position: absolute; left: 171px; top: 290px;
    font-family: "Michroma", sans-serif;
    font-size: 31px; letter-spacing: 5px;
    color: var(--graphite);
    line-height: 1;
  }
  .front-kiss {
    position: absolute; left: 507px; top: 283px;
    width: 200px; height: 146px;
  }

  .back-kiss {
    position: absolute; left: 0; top: 0;
    width: 275px; height: 272px;
  }
  .back-rule {
    position: absolute; left: 272px; right: 0; top: 123px;
    height: 2px; background: var(--rule);
  }
  .back-company {
    position: absolute; right: 88px; top: 134px;
    font-family: "Michroma", sans-serif;
    font-size: 21px; letter-spacing: 2px;
    color: var(--graphite);
    line-height: 1;
  }
  .contact {
    position: absolute; right: 88px;
    text-align: right;
    font-size: 20px; line-height: 27px;
    color: var(--graphite);
  }
  .contact--address { top: 177px; }
  .contact--reach { top: 258px; }

  .web-band {
    position: absolute; left: 0; top: 350px;
    width: 718px; height: 105px;
  }
  .web-url {
    position: absolute; right: 86px; top: 388px;
    font-weight: 700; font-size: 29px;
    color: #ffffff; line-height: 1;
  }
</style>
</head>
<body>

  <section class="card card--front">
    <div class="front-rule"></div>
    <div class="front-name">VELTRINAR</div>
    <svg class="front-kiss" viewBox="0 0 200 146" role="img" aria-label="Illustration: roter Lippenstift-Kussabdruck">
      <defs>
        <linearGradient id="kissFront" x1="0" y1="0" x2="1" y2="1">
          <stop offset="0" stop-color="#e8709a"/>
          <stop offset="1" stop-color="#d8244f"/>
        </linearGradient>
      </defs>
      <ellipse cx="100" cy="73" rx="96" ry="62" fill="url(#kissFront)"/>
    </svg>
  </section>

  <section class="card card--back">
    <svg class="back-kiss" viewBox="0 0 275 272" role="img" aria-label="Illustration: zartrosa Kussabdruck, angeschnitten">
      <defs>
        <linearGradient id="kissBack" x1="0" y1="0" x2="1" y2="1">
          <stop offset="0" stop-color="#f6c6d6"/>
          <stop offset="1" stop-color="#eea3b1"/>
        </linearGradient>
      </defs>
      <ellipse cx="110" cy="130" rx="165" ry="140" fill="url(#kissBack)"/>
    </svg>
    <div class="back-rule"></div>
    <div class="back-company">VELTRINAR GMBH</div>
    <div class="contact contact--address">80469 Lindtal<br>Ahornweg 17</div>
    <div class="contact contact--reach">0171 - 42 58 93 1<br>hallo@autowerk-rosa.de</div>
    <svg class="web-band" viewBox="0 0 718 105" preserveAspectRatio="none" aria-hidden="true">
      <defs>
        <linearGradient id="bandFill" x1="0" y1="0" x2="1" y2="0">
          <stop offset="0" stop-color="var(--band-start)"/>
          <stop offset="1" stop-color="var(--band-end)"/>
        </linearGradient>
      </defs>
      <path d="M0 26 L120 18 L260 12 L400 8 L520 10 L640 16 L718 20 L718 105 L620 100 L480 96 L340 94 L200 96 L80 98 L0 100 Z" fill="url(#bandFill)"/>
    </svg>
    <div class="web-url">www.autowerk-rosa.de</div>
  </section>

</body>
</html>
```